Email Banner (QuillStacks)

We require an email banner for our email promotions sent to prospect clients. The banner needs to contain the wording QuillStacks and use the same colour scheme as the logos attached.

This is for B2B professional's so needs to look like a place you would come to read technology articles.

```html
<!DOCTYPE html>
<html lang="en">
<head>
<meta charset="utf-8">
<title>QuillStacks Email Banners</title>
<link href="https://fonts.googleapis.com/css2?family=Urbanist:wght@700&display=swap" rel="stylesheet">
<style>
  :root {
    --navy: #23375a;
    --red: #cd2a2f;
    --crimson: #b42340;
    --magenta: #991a4e;
    --wordmark: #cfd0d2;
    --accent-light: #d6d7da;
    --page: #ffffff;
  }
  html, body {
    margin: 0;
    padding: 0;
    width: 1200px;
    height: 960px;
    overflow: hidden;
    background: var(--page);
  }
  .canvas {
    position: relative;
    width: 1200px;
    height: 960px;
  }
  .banner {
    position: absolute;
    left: 97px;
    width: 1010px;
    height: 337px;
    display: block;
  }
  .banner--red-centre { top: 99px; }
  .banner--navy-centre { top: 527px; }
  .wordmark {
    font-family: "Urbanist", "Helvetica Neue", Arial, sans-serif;
    font-weight: 700;
    font-size: 146px;
    letter-spacing: -1px;
    fill: var(--wordmark);
  }
</style>
</head>
<body>
<main class="canvas">

  <svg class="banner banner--red-centre" viewBox="0 0 1810 603" preserveAspectRatio="none" aria-label="QuillStacks email banner, red band">
    <defs>
      <radialGradient id="bandGlow" cx="900" cy="320" r="1000" gradientTransform="translate(900 320) scale(1 0.55) translate(-900 -320)" gradientUnits="userSpaceOnUse">
        <stop offset="0" stop-color="var(--red)"/>
        <stop offset="0.55" stop-color="var(--crimson)"/>
        <stop offset="1" stop-color="var(--magenta)"/>
      </radialGradient>
      <linearGradient id="decorSoftNavy" x1="0" y1="480" x2="440" y2="40" gradientUnits="userSpaceOnUse">
        <stop offset="0" stop-color="var(--accent-light)" stop-opacity="0"/>
        <stop offset="1" stop-color="var(--accent-light)" stop-opacity="0.14"/>
      </linearGradient>
    </defs>
    <rect width="1810" height="603" fill="var(--navy)"/>
    <polygon points="602,0 1810,0 1208,603 0,603" fill="url(#bandGlow)"/>
    <polygon class="decor-area" role="img" aria-label="Circuit-line technology decoration" points="0,40 440,40 0,480" fill="url(#decorSoftNavy)"/>
    <polygon class="decor-area" role="img" aria-label="Circuit-line technology decoration" points="1810,563 1370,563 1810,123" fill="url(#decorSoftNavy)" transform="rotate(180 1590 343)" transform-origin="0 0" style="transform: rotate(180deg); transform-box: fill-box; transform-origin: center;"/>
    <text class="wordmark" x="901" y="352" text-anchor="middle">QuillStacks</text>
  </svg>

  <svg class="banner banner--navy-centre" viewBox="0 0 1810 603" preserveAspectRatio="none" aria-label="QuillStacks email banner, navy band">
    <defs>
      <linearGradient id="cornerLeft" x1="0" y1="0" x2="0" y2="603" gradientUnits="userSpaceOnUse">
        <stop offset="0" stop-color="var(--red)"/>
        <stop offset="1" stop-color="var(--magenta)"/>
      </linearGradient>
      <linearGradient id="cornerRight" x1="0" y1="0" x2="0" y2="603" gradientUnits="userSpaceOnUse">
        <stop offset="0" stop-color="var(--magenta)"/>
        <stop offset="1" stop-color="var(--red)"/>
      </linearGradient>
      <linearGradient id="decorSoftRed" x1="0" y1="480" x2="440" y2="40" gradientUnits="userSpaceOnUse">
        <stop offset="0" stop-color="var(--accent-light)" stop-opacity="0"/>
        <stop offset="1" stop-color="var(--accent-light)" stop-opacity="0.16"/>
      </linearGradient>
    </defs>
    <rect width="1810" height="603" fill="var(--navy)"/>
    <polygon points="0,0 602,0 0,603" fill="url(#cornerLeft)"/>
    <polygon points="1810,0 1810,603 1208,603" fill="url(#cornerRight)"/>
    <polygon class="decor-area" role="img" aria-label="Circuit-line technology decoration" points="0,40 440,40 0,480" fill="url(#decorSoftRed)"/>
    <polygon class="decor-area" role="img" aria-label="Circuit-line technology decoration" points="1810,563 1370,563 1810,123" fill="url(#decorSoftRed)" style="transform: rotate(180deg); transform-box: fill-box; transform-origin: center;"/>
    <text class="wordmark" x="901" y="352" text-anchor="middle">QuillStacks</text>
  </svg>

</main>
</body>
</html>
```